Real Estate Business Cards

Looking for a clean, sharp and professional look for our Real Estate investment Fund that invests in Multi Family Apartment buildings.

Target Market(s)

Real Estate Fund

Industry/Entity Type

Real Estate

Contact Information for Business Card

Company Description: Real Estate Investment Fund
Company Name: RKW Holdings
Name: Marcus Olvane
Cell: (917) 482-0657
Email: marcus@rkwholdings-example.com
Website: www.rkwholdings-example.com
Address: 418, 9th Street, Brooklyn NY 11218

Colors

Designer to choose colors to be used in the design.

Requirements
Nice to have
• Colors to match logo

```html
<!DOCTYPE html>
<html lang="en">
<head>
<meta charset="utf-8">
<title>RKW Holdings — Business Cards</title>
<link rel="stylesheet" href="https://fonts.googleapis.com/css2?family=Crimson+Pro:ital,wght@0,600;1,600;1,700&family=Open+Sans:wght@700&display=swap">
<style>
  :root {
    --backdrop: #d6d7d9;
    --card: #363538;
    --brand-blue: #2479b5;
    --brand-grey: #56555a;
    --text-light: #f4f4f4;
    --icon-blue: #2a86c8;
  }
  * { box-sizing: border-box; margin: 0; padding: 0; }
  html, body {
    width: 1200px;
    height: 800px;
    overflow: hidden;
    background: var(--backdrop);
  }
  .canvas {
    position: relative;
    width: 1200px;
    height: 800px;
  }
  .card {
    position: absolute;
    top: 280px;
    width: 420px;
    height: 240px;
    border-radius: 14px;
    background: var(--card);
    overflow: hidden;
  }
  .card--front { left: 150px; }
  .card--back  { left: 630px; }

  .brand {
    position: absolute;
    display: flex;
    align-items: center;
    gap: 10px;
  }
  .brand__mark {
    width: 26px;
    height: 26px;
    background: var(--brand-blue);
  }
  .brand__name {
    font-family: "Crimson Pro", Georgia, serif;
    font-weight: 600;
    font-size: 26px;
    letter-spacing: 0.5px;
    color: var(--brand-blue);
  }
  .card--front .brand { left: 104px; top: 78px; }

  .tagline {
    position: absolute;
    left: 104px;
    top: 138px;
    font-family: "Crimson Pro", Georgia, serif;
    font-style: italic;
    font-weight: 700;
    font-size: 23px;
    color: var(--text-light);
  }

  .card--back .brand { left: 26px; top: 52px; }
  .card--back .brand__mark { background: var(--brand-grey); width: 20px; height: 20px; }
  .card--back .brand__name { color: var(--brand-grey); font-size: 20px; }

  .person-name {
    position: absolute;
    right: 34px;
    top: 22px;
    font-family: "Crimson Pro", Georgia, serif;
    font-weight: 600;
    font-size: 21px;
    letter-spacing: 0.8px;
    text-transform: uppercase;
    color: var(--brand-blue);
  }

  .contact {
    position: absolute;
    left: 222px;
    top: 120px;
    list-style: none;
    font-family: "Open Sans", Arial, sans-serif;
    font-weight: 700;
    font-size: 10.5px;
    line-height: 15px;
    color: var(--text-light);
  }
  .contact__item {
    display: flex;
    align-items: flex-start;
    gap: 7px;
  }
  .contact__icon {
    flex: none;
    margin-top: 3px;
    width: 8px;
    height: 8px;
  }
</style>
</head>
<body>
<main class="canvas">

  <section class="card card--front" aria-label="Business card front">
    <div class="brand">
      <span class="brand__mark"></span>
      <span class="brand__name">RKW Holdings</span>
    </div>
    <p class="tagline">Real Estate Investment Fund</p>
  </section>

  <section class="card card--back" aria-label="Business card back">
    <div class="brand">
      <span class="brand__mark"></span>
      <span class="brand__name">RKW Holdings</span>
    </div>
    <h1 class="person-name">Marcus Olvane</h1>
    <ul class="contact">
      <li class="contact__item">
        <svg class="contact__icon" viewBox="0 0 8 8" aria-hidden="true"><circle cx="4" cy="4" r="4" fill="var(--icon-blue)"/><rect x="2.5" y="1.8" width="3" height="4.4" rx="0.6" fill="var(--card)"/></svg>
        <span>(917) 482-0657</span>
      </li>
      <li class="contact__item">
        <svg class="contact__icon" viewBox="0 0 8 8" aria-hidden="true"><circle cx="4" cy="4" r="4" fill="var(--icon-blue)"/><rect x="2" y="2.6" width="4" height="2.8" fill="var(--card)"/></svg>
        <span>marcus@rkwholdings-example.com</span>
      </li>
      <li class="contact__item">
        <svg class="contact__icon" viewBox="0 0 8 8" aria-hidden="true"><circle cx="4" cy="4" r="4" fill="var(--icon-blue)"/><path d="M4 1.6a1.5 1.5 0 0 1 1.5 1.5C5.5 4.3 4 6.2 4 6.2S2.5 4.3 2.5 3.1A1.5 1.5 0 0 1 4 1.6z" fill="var(--card)"/></svg>
        <span>418, 9th Street,<br>Brooklyn NY 11218</span>
      </li>
      <li class="contact__item">
        <svg class="contact__icon" viewBox="0 0 8 8" aria-hidden="true"><circle cx="4" cy="4" r="4" fill="var(--icon-blue)"/><circle cx="4" cy="4" r="2" fill="none" stroke="var(--card)" stroke-width="0.8"/></svg>
        <span>www.rkwholdings-example.com</span>
      </li>
    </ul>
  </section>

</main>
</body>
</html>
```